Plakat/Handzettel für Bildungs- und Gesundheitsservice
Zielgruppe
Wir benötigen eine Datei, die wir als
a.) Handzettel (DIN A4) sowie
b.) als Poster (DIN A1) ausdrucken können.
ACHTUNG:
a.) bitte in einem Format liefern, in dem den CODE XXXX immer 'selbst' austauschen können. Handzettel kann als Word-Datei.. das Poster lieber in einem Format, was mit Photoshop ggf. aufrufbar ist (weil wir den Code auf jedem Poster ändern müssen)
b.) Anliegend der Text der auf das Poster und Handzettel muss.
Aufgabenstellung
siehe Farben Website www.lindquel-akadem.com
bitte selbst entscheiden, ob Fotos auf dem Poster bzw. Handzettel sein sollen.

```html
<!DOCTYPE html>
<html lang="de">
<head>
<meta charset="utf-8">
<title>Lindquel Akadem – Handzettel</title>
<link href="https://fonts.googleapis.com/css2?family=Oswald:wght@300;400&family=Montserrat:ital,wght@0,400;0,600;0,700;1,600;1,700&family=Open+Sans:ital,wght@0,400;1,600&display=swap" rel="stylesheet">
<style>
  :root {
    --ink: #1d1f24;
    --blue: #3a7bbd;
    --sky: #5fb9d4;
    --sky-dark: #4fa9c7;
    --band-a: #2f6aa6;
    --band-b: #3d80b6;
    --paper-a: #f7f8f9;
    --paper-b: #eef1f4;
    --quote-grey: #cfd3d8;
    --white: #ffffff;
  }
  * { box-sizing: border-box; margin: 0; padding: 0; }
  html, body { width: 750px; height: 1200px; overflow: hidden; background: var(--paper-a); }
  .flyer {
    position: relative; width: 750px; height: 1200px; overflow: hidden;
    background: linear-gradient(180deg, var(--paper-a), var(--paper-b));
    font-family: 'Montserrat', sans-serif; color: var(--ink);
  }
  .hero-photo {
    position: absolute; right: 0; top: 0; width: 420px; height: 540px;
    background:
      linear-gradient(90deg, var(--paper-a) 0%, rgba(247,248,249,0) 35%),
      linear-gradient(0deg, var(--paper-a) 0%, rgba(247,248,249,0) 30%),
      linear-gradient(160deg, #dfe8ef 0%, #b9c6d2 45%, #6d7886 75%, #cfd9e2 100%);
  }
  .brand {
    position: absolute; left: 60px; top: 120px; width: 280px;
    display: flex; align-items: center; justify-content: center; gap: 10px;
  }
  .brand-mark { width: 14px; height: 14px; background: var(--ink); }
  .brand-name { font-size: 19px; font-weight: 400; letter-spacing: 4px; color: var(--ink); }
  .headline {
    position: absolute; left: 62px; top: 222px;
    font-family: 'Oswald', sans-serif; font-weight: 300; line-height: 1.13;
  }
  .headline .main { font-size: 64px; color: var(--ink); display: block; }
  .headline .sub { font-size: 40px; color: var(--blue); display: block; margin-top: 4px; font-weight: 400; }
  .access-card {
    position: absolute; left: 48px; top: 557px; width: 312px; height: 281px;
    background: var(--sky); border-radius: 20px; color: var(--white); text-align: center;
    padding: 28px 20px 0;
  }
  .access-title { font-size: 17px; font-weight: 700; line-height: 1.35; }
  .access-hint { font-family: 'Open Sans', sans-serif; font-size: 15px; margin-top: 22px; }
  .code-field {
    margin: 10px auto 0; width: 270px; height: 50px; background: var(--white);
    color: var(--blue); font-weight: 700; font-size: 20px; line-height: 50px;
  }
  .access-register { font-family: 'Open Sans', sans-serif; font-size: 14px; margin-top: 20px; }
  .access-url { font-family: 'Open Sans', sans-serif; font-style: italic; font-weight: 600; font-size: 12.5px; margin-top: 4px; }
  .quote {
    position: absolute; left: 40px; top: 905px; width: 340px; text-align: center;
    transform: rotate(-3deg); font-style: italic; font-weight: 700; font-size: 19px; line-height: 1.4;
  }
  .quote-mark {
    position: absolute; left: 0; top: -42px; font-family: Georgia, serif; font-size: 150px;
    color: var(--quote-grey); font-style: normal; line-height: 1; z-index: 0;
  }
  .quote p { position: relative; z-index: 1; }
  .quote .accent { color: var(--sky-dark); }
  .offers { position: absolute; left: 418px; top: 568px; width: 320px; }
  .offer { margin-bottom: 24px; }
  .offer h2 { font-size: 19px; font-weight: 700; line-height: 1.4; text-transform: uppercase; }
  .offer h2 .hl { color: var(--blue); }
  .offer ul { list-style: none; margin-top: 12px; }
  .offer li { font-size: 17px; line-height: 1.7; padding-left: 24px; position: relative; }
  .offer li::before {
    content: ""; position: absolute; left: 4px; top: 11px; width: 7px; height: 7px;
    border-radius: 50%; background: var(--sky);
  }
  .topic-grid { display: grid; grid-template-columns: 152px 1fr; }
  .topic-grid ul { margin-top: 12px; }
  .footer-band {
    position: absolute; left: 0; bottom: 0; width: 750px; height: 66px;
    background: linear-gradient(90deg, var(--band-a), var(--band-b));
    color: var(--white); font-weight: 700; font-size: 17px; letter-spacing: 0.5px;
    display: flex; align-items: center; justify-content: center;
  }
</style>
</head>
<body>
<main class="flyer">
  <div class="hero-photo" role="img" aria-label="Foto: lächelnde Dozentin am Rednerpult mit Laptop in hellem Raum"></div>

  <div class="brand">
    <span class="brand-mark"></span>
    <span class="brand-name">LINDQUEL AKADEM</span>
  </div>

  <h1 class="headline">
    <span class="main">HUNDERTE VON<br>ABENDLICHEN<br>UNIVERSITÄREN</span>
    <span class="sub">LIVE-VERANSTALTUNGEN</span>
  </h1>

  <section class="access-card">
    <p class="access-title">ZUGANG ZUM VIRTUELLEN HÖRSAAL AUF DER LINDQUEL AKADEM:</p>
    <p class="access-hint">Ihr Code für eine kostenfreie Nutzung:</p>
    <div class="code-field">CODE XXXX</div>
    <p class="access-register">Melden Sie sich an:</p>
    <p class="access-url">www.portal.lindquelakadem.com/register</p>
  </section>

  <blockquote class="quote">
    <span class="quote-mark">“</span>
    <p>Wir öffnen die Türen zum virtuellen Hörsaal für „alle“ Mitarbeitende,<br>
    <span class="accent">denn bei uns ist wissen-<br>schaftliche Bildung für alle da.</span></p>
  </blockquote>

  <section class="offers">
    <div class="offer">
      <h2>Live-<span class="hl">Vorlesungen</span> von 150 Professorinnen und Professoren</h2>
      <div class="topic-grid">
        <ul>
          <li>Gesundheit</li>
          <li>Psychologie</li>
          <li>Medizin</li>
          <li>Marketing</li>
        </ul>
        <ul>
          <li>Führung</li>
          <li>und viele weitere Themen</li>
        </ul>
      </div>
    </div>
    <div class="offer">
      <h2>Live-praktische <span class="hl">Seminare</span></h2>
      <ul>
        <li>Prävention von Burnout</li>
        <li>Resilienz Training</li>
        <li>Und viele weitere Themen</li>
      </ul>
    </div>
    <div class="offer">
      <h2>Live-<span class="hl">Dialogrunden</span></h2>
      <ul>
        <li>Prävention von Burnout</li>
        <li>Resilienz Training</li>
        <li>Und viele weitere Themen</li>
      </ul>
    </div>
  </section>

  <footer class="footer-band">WWW.LINDQUEL-AKADEM.COM</footer>
</main>
</body>
</html>
```